QM - menu design

Hi,

We require elegant menu design for upscale restaurant. Please find attached the logo and the menu items for your reference.

for inspiration, this is a good website: -
http://www.plivermark.com/tablefolio/about.php

We are very much open for Menu Size suggestions.

unfortunately the place is going under renovation, we don't have updated images to it. the closest look and feel to our place is http://vessora.com ..

we are also open for creative options on the shape, the styles, etc. as long as it represents the fine dine feel ...

Thanks ...
Updates

Dear All,

We wouldlike to extend our apology for not being able to provide feedbacks on everysingle design. We were extremely busy and we have multiple contests opensimultaneously which makes the process even harder.

However,we would like to thank you all for the efforts you have put into designingour menu. It is very much appreciated …

We wishyou all success in your design ventures and we are quite positive that we willbe working with many of you on many projects in the soon future. 

Thanks & Regards,

DHI Team...

 

 

 

Industry/Entity Type

Restaurant

Requirements
Must have
• Please ensure that there are 'some' images in the menu ... this is very important.
Should not have
• IMPORTANT: -

1. Please DO NOT insert any currency sign to the menu
2. Please keep the prices of the menu at the end of the menu items descriptions NOT beside the menu item names. The font of the price should be similar to the menu item description and please DO NOT bold the numbers. the prices should be subtle.

Thank you ...

```html
<!DOCTYPE html>
<html lang="en">
<head>
<meta charset="utf-8">
<title>Breakfast and Sandwiches Menu Spread</title>
<link href="https://fonts.googleapis.com/css2?family=Mulish:wght@300;400;700&family=Questrial&display=swap" rel="stylesheet">
<style>
  :root {
    --backdrop: #e4e4e4;
    --page: #4b4b4d;
    --page-deep: #3f3f41;
    --gold: #eab73a;
    --ink: #e6e6e6;
    --ink-soft: #cfcfcf;
    --bread: #d7a259;
    --egg: #f3c43a;
    --tomato: #c8352c;
    --lettuce: #7aa744;
    --edge: #b98c4a;
  }
  * { box-sizing: border-box; margin: 0; padding: 0; }
  html, body { width: 1200px; height: 690px; overflow: hidden; }
  body {
    background: var(--backdrop);
    font-family: "Mulish", "Century Gothic", sans-serif;
    color: var(--ink);
  }
  .spread {
    position: absolute;
    left: 40px; top: 40px;
    width: 1120px; height: 610px;
    display: flex;
    box-shadow: 0 4px 18px rgba(0,0,0,0.18);
  }
  .page {
    position: relative;
    width: 560px; height: 610px;
    display: flex;
  }
  .page--left { background: linear-gradient(90deg, var(--page) 85%, var(--page-deep) 100%); }
  .page--right { background: linear-gradient(90deg, var(--page-deep) 0%, var(--page) 15%); }
  .photo { width: 140px; height: 100%; flex: none; }
  .photo--breakfast {
    background: linear-gradient(180deg, #f2a623 0%, var(--bread) 22%, #b87a3c 48%, var(--egg) 68%, #f7e08c 100%);
    border-right: 3px solid var(--edge);
  }
  .photo--sandwich {
    background: linear-gradient(180deg, var(--tomato) 0%, #a8282a 14%, var(--bread) 30%, #e7c995 48%, var(--lettuce) 58%, #e6a9a0 70%, #c9b9a6 88%, #2b2b2b 100%);
    border-left: 3px solid var(--edge);
  }
  .menu-column { flex: 1; padding: 26px 26px 0 26px; }
  .page--right .menu-column { padding-left: 34px; }
  .section-title {
    font-family: "Questrial", "Century Gothic", sans-serif;
    font-weight: 400;
    font-size: 26px;
    color: #f2f2f2;
    margin-bottom: 14px;
  }
  .section-title--soup { margin-top: 20px; font-size: 28px; }
  .dish { margin-bottom: 11px; font-size: 12.5px; line-height: 1.22; color: var(--ink-soft); }
  .dish-name { display: block; font-weight: 700; font-size: 14px; color: var(--gold); }
  .dish-name--inline { display: inline; font-size: 12.5px; }
  .price { font-weight: 400; color: var(--gold); }
</style>
</head>
<body>
  <main class="spread">
    <section class="page page--left">
      <div class="photo photo--breakfast" role="img" aria-label="Photo of toasted bread and scrambled eggs with basil"></div>
      <div class="menu-column">
        <h2 class="section-title">The Breakfast</h2>
        <p class="dish"><span class="dish-name">Butter Croissant</span>Served plain with a selection of two jams, a vanilla custard cream, a chocolate Cream and butter curls). <span class="price">36</span></p>
        <p class="dish"><span class="dish-name">Cheese Croissant</span>Crumbly freshly baked with cheese filling. <span class="price">29</span></p>
        <p class="dish"><span class="dish-name">Daily Fresh Eggs</span>A choice of poached, scrambled, pan fried, omelet) all served with toasted Bread, mushrooms, roasted tomatoes and chicken sausages. <span class="price">59</span></p>
        <p class="dish"><span class="dish-name">Healthy Time</span>One choice of hot beverage from our cafe served with fruit salad, natural Yoghurt, whole wheat bread vegetable sandwiches and sugar free biscuits selection.<span class="price">49</span></p>
        <p class="dish"><span class="dish-name">Energy Time</span>One choice of hot beverage from our cafe served with finger chocolate muffins, Poached egg with toasted bread and crispy beef bacon, crepe roll with goat Cheese and honey and finger chocolate cream with salted cookies. <span class="price">59</span></p>
        <p class="dish"><span class="dish-name">Third Avenue Time</span>One choice of hot beverage from our cafe served with our selection of scones, Smoked salmon and avocado sandwich, roasted sausages sandwich, grilled vegetables sandwich, selection of our best biscuits. <span class="price">59</span></p>
        <p class="dish"><span class="dish-name">The Arabic Breakfast</span>Choice of Zattar Manakish and Cheese Manakish, served with one choice of hot beverage from our cafe and fresh orange juice. <span class="price">59</span></p>
      </div>
    </section>
    <section class="page page--right">
      <div class="menu-column">
        <h2 class="section-title">The Sandwiches</h2>
        <p class="dish"><span class="dish-name dish-name--inline">Grilled Vegetables Sandwich</span> with fresh Goat cheese and chives served with our Homemade spicy garlic mayo. <span class="price">59</span></p>
        <p class="dish"><span class="dish-name dish-name--inline">Butterfish burger</span> with fresh tomato, beef bacon, grilled vegetables and béarnaise sauce.</p>
        <p class="dish"><span class="dish-name dish-name--inline">Tataki Tuna sandwich</span> with red onion slices, stewed endives and black olives and sultanas pate'. <span class="price">79</span></p>
        <p class="dish"><span class="dish-name dish-name--inline">Beef sirloin</span> steak sandwich with grain mustard, Parmesan cheese and fresh Nashi pears. <span class="price">79</span></p>
        <p class="dish"><span class="dish-name dish-name--inline">The Traditional Club</span> sandwich served with French fries and vegetable chips. <span class="price">69</span></p>
        <p class="dish"><span class="dish-name dish-name--inline">Chicken sandwich</span> with Parmesan cheese slices, sundried tomatoes and mint Flavored mayo. <span class="price">69</span></p>
        <h2 class="section-title section-title--soup">Soup</h2>
        <p class="dish"><span class="dish-name">Bouillabaisse</span>Traditional French Seafood soup, with Saffron and Estragon. <span class="price">119</span></p>
        <p class="dish"><span class="dish-name">Barley soup</span>With fresh vegetables, tomato smoothie and a hint of garlic oil. <span class="price">49</span></p>
        <p class="dish"><span class="dish-name">Beef chili</span>Served with Arabic bread, fresh guacamole and spicy black beans. <span class="price">49</span></p>
      </div>
      <div class="photo photo--sandwich" role="img" aria-label="Photo of a baguette sandwich with tomato, lettuce and ham"></div>
    </section>
  </main>
</body>
</html>
```